Banner for fencing on construction sites

Banner to market our company on construction job sites Included on banner we would need something along the lines "Temp Labor" and our website "WWW.KTRVB.COM" all Visible enough to see as people are driving by.
The attached .ai file we provided has two images, we prefer the 2nd one with just RVB.
The Banner will be 7ft wide x 4ft height.

Target Market(s)

Construction Companies

Requirements
Must have
• Visible Website to drivers passing by
• RVB Logo has to be BIGGER than anything

```html
<!DOCTYPE html>
<html lang="en">
<head>
<meta charset="utf-8">
<title>RVB Temp Labor – Site Fencing Banner</title>
<link rel="stylesheet" href="https://fonts.googleapis.com/css2?family=Anton&family=Oswald:wght@600&display=swap">
<style>
  :root {
    --stage: #6b6b6b;
    --ink-white: #ffffff;
    --brand-orange: #f7a23a;
    --logo-orange: #f5902e;
    --night-blue: #18486f;
    --deep-blue: #0d2740;
    --black: #000000;
    --sun-cream: #fbe6b8;
    --steel-amber: #b7762e;
    --steel-brown: #3a2210;
  }
  html, body {
    margin: 0;
    padding: 0;
    width: 1200px;
    height: 1200px;
    overflow: hidden;
    background: var(--stage);
  }
  .stage {
    position: relative;
    width: 1200px;
    height: 1200px;
  }
  .banner {
    position: absolute;
    overflow: hidden;
    box-shadow: 6px 8px 18px rgba(0, 0, 0, 0.45);
  }
  .banner--dusk { left: 174px; top: 70px; width: 854px; height: 488px; }
  .banner--steel { left: 176px; top: 643px; width: 848px; height: 485px; }

  .banner__scene {
    position: absolute;
    inset: 0;
  }
  .banner--dusk .banner__scene {
    background: linear-gradient(180deg, var(--night-blue) 0%, var(--deep-blue) 45%, var(--black) 78%, var(--black) 100%);
  }
  .banner--steel .banner__scene {
    background:
      linear-gradient(180deg, rgba(0,0,0,0) 0%, rgba(0,0,0,0) 50%, rgba(0,0,0,0.85) 74%, var(--black) 86%),
      linear-gradient(100deg, var(--steel-brown) 0%, var(--steel-amber) 40%, var(--sun-cream) 85%);
  }

  .banner__content {
    position: absolute;
    inset: 0;
    text-align: center;
  }
  .brand-name {
    position: absolute;
    left: 0;
    right: 0;
    top: 28px;
    margin: 0;
    font-family: "Anton", "Impact", sans-serif;
    font-weight: 400;
    font-size: 200px;
    line-height: 1;
    letter-spacing: 4px;
    color: var(--logo-orange);
  }
  .web-address {
    position: absolute;
    left: 0;
    right: 0;
    top: 284px;
    margin: 0;
    font-family: "Anton", "Impact", sans-serif;
    font-weight: 400;
    font-size: 96px;
    line-height: 1.05;
    color: var(--ink-white);
    letter-spacing: 1px;
  }
  .web-address__brand { color: var(--brand-orange); }
  .service-line {
    position: absolute;
    left: 0;
    right: 0;
    top: 396px;
    margin: 0;
    font-family: "Oswald", "Arial Narrow", sans-serif;
    font-weight: 600;
    font-size: 52px;
    line-height: 1.2;
    color: var(--brand-orange);
    word-spacing: 2px;
  }
  .service-line__phone { margin-left: 28px; }
</style>
</head>
<body>
<main class="stage">

  <section class="banner banner--dusk">
    <div class="banner__scene" role="img" aria-label="Photo of a tower crane silhouetted against a deep blue dusk sky"></div>
    <div class="banner__content">
      <h1 class="brand-name">RVB</h1>
      <p class="web-address">WWW.KT<span class="web-address__brand">RVB</span>.COM</p>
      <p class="service-line">Temp Labor<span class="service-line__phone">000-000-0000</span></p>
    </div>
  </section>

  <section class="banner banner--steel">
    <div class="banner__scene" role="img" aria-label="Photo of a steel building frame backlit by warm golden sunlight"></div>
    <div class="banner__content">
      <h2 class="brand-name">RVB</h2>
      <p class="web-address">WWW.KT<span class="web-address__brand">RVB</span>.COM</p>
      <p class="service-line">Temp Labor<span class="service-line__phone">000-000-0000</span></p>
    </div>
  </section>

</main>
</body>
</html>
```